I need a bushiness card designed for my business Kind Sparrow Club attached is the logo
On the business cards I would like the following info
427 Hollister Ln #3085
Larkfield Tx, 77519
555-481-5527
Please free free to be creative, our business targets girls 6-11 years old, a hip and cool looking card is what we are looking for to be passed out at a girls event.......Thanks

```html
<!DOCTYPE html>
<html lang="en">
<head>
<meta charset="utf-8">
<title>Kind Sparrow Club – Business Card</title>
<link rel="stylesheet" href="https://fonts.googleapis.com/css2?family=Josefin+Sans:wght@300;700&display=swap">
<style>
  :root {
    --backdrop: #2b2b2b;
    --card-white: #ffffff;
    --panel-blue: #4fa7c9;
    --ink-white: #ffffff;
    --pink: #e8197f;
    --orange: #f7941d;
    --teal: #3fa9c5;
    --purple: #8a4f9e;
  }
  * { margin: 0; padding: 0; box-sizing: border-box; }
  html, body {
    width: 960px; height: 1200px; overflow: hidden;
    background: var(--backdrop);
    font-family: "Josefin Sans", sans-serif;
  }
  .stage { position: relative; width: 960px; height: 1200px; }

  .card {
    position: absolute;
    left: 158px;
    width: 651px;
    background: var(--card-white);
    overflow: hidden;
  }
  .card--front { top: 126px; height: 420px; }
  .card--back { top: 640px; height: 422px; }

  .dot-field {
    position: absolute;
    background:
      radial-gradient(circle at 15% 30%, rgba(232,25,127,.7), transparent 40%),
      radial-gradient(circle at 80% 75%, rgba(247,148,29,.7), transparent 40%),
      radial-gradient(circle at 50% 55%, rgba(63,169,197,.6), transparent 45%),
      radial-gradient(circle at 88% 20%, rgba(138,79,158,.6), transparent 40%),
      radial-gradient(circle at 35% 85%, rgba(138,79,158,.5), transparent 35%),
      #f4cfe0;
  }
  .card--front .dot-field { inset: 0; }
  .card--back .dot-field { left: 0; right: 0; bottom: 0; height: 130px; }

  .contact-panel {
    position: absolute;
    left: 52px; top: 48px;
    width: 547px; height: 322px;
    background: var(--panel-blue);
    box-shadow: 0 2px 6px rgba(0,0,0,.25);
    color: var(--ink-white);
  }
  .contact-row {
    position: absolute;
    left: 70px;
    font-weight: 300;
    font-size: 31px;
    line-height: 44px;
    white-space: nowrap;
  }
  .contact-row--address { top: 8px; }
  .contact-row--phone { top: 126px; }
  .contact-row--social { top: 198px; left: 58px; font-size: 30px; }
  .contact-row--web { top: 270px; left: 62px; }

  .divider {
    position: absolute;
    left: 70px; width: 466px; height: 2px;
    background: var(--ink-white);
  }
  .divider--1 { top: 112px; }
  .divider--2 { top: 188px; }
  .divider--3 { top: 262px; }

  .icon { position: absolute; fill: var(--ink-white); }
  .icon--pin { left: 20px; top: 26px; }
  .icon--phone { left: 22px; top: 128px; }
  .icon--social { left: 18px; top: 204px; }
  .icon--globe { left: 16px; top: 272px; }

  .brand {
    position: absolute;
    left: 0; right: 0; top: 62px;
    display: flex; align-items: center; justify-content: center; gap: 20px;
  }
  .brand-mark {
    width: 40px; height: 40px; border-radius: 50%;
    background: var(--purple);
  }
  .brand-name {
    font-weight: 700;
    font-size: 66px;
    line-height: 1.1;
    color: var(--pink);
    text-align: center;
  }
</style>
</head>
<body>
<main class="stage">

  <section class="card card--front">
    <div class="dot-field" role="img" aria-label="Colourful polka-dot pattern in pink, orange, teal and purple"></div>
    <div class="contact-panel">
      <svg class="icon icon--pin" width="26" height="36" viewBox="0 0 26 36" aria-hidden="true">
        <path d="M13 0C5.8 0 0 5.8 0 13c0 9.5 13 23 13 23s13-13.5 13-23C26 5.8 20.2 0 13 0zm0 18a5 5 0 1 1 0-10 5 5 0 0 1 0 10z"/>
      </svg>
      <p class="contact-row contact-row--address">427 Hollister Ln #3085<br>Larkfield Tx, 77519</p>
      <div class="divider divider--1"></div>

      <svg class="icon icon--phone" width="24" height="40" viewBox="0 0 24 40" aria-hidden="true">
        <path d="M4 0h16a4 4 0 0 1 4 4v32a4 4 0 0 1-4 4H4a4 4 0 0 1-4-4V4a4 4 0 0 1 4-4zm-1 6v26h18V6zm9 28a2 2 0 1 0 0 4 2 2 0 0 0 0-4z"/>
      </svg>
      <p class="contact-row contact-row--phone">555-481-5527</p>
      <div class="divider divider--2"></div>

      <svg class="icon icon--social" width="32" height="32" viewBox="0 0 32 32" aria-hidden="true">
        <rect width="32" height="32" rx="3"/>
      </svg>
      <p class="contact-row contact-row--social">www.pallink.com/kindsparrowclub</p>
      <div class="divider divider--3"></div>

      <svg class="icon icon--globe" width="38" height="38" viewBox="0 0 38 38" aria-hidden="true">
        <g fill="none" stroke="#fff" stroke-width="2.2">
          <circle cx="19" cy="19" r="17"/>
          <ellipse cx="19" cy="19" rx="8" ry="17"/>
          <line x1="2" y1="19" x2="36" y2="19"/>
          <path d="M5 10h28M5 28h28"/>
        </g>
      </svg>
      <p class="contact-row contact-row--web">www.kindsparrowclub.net</p>
    </div>
  </section>

  <section class="card card--back">
    <div class="brand">
      <span class="brand-mark" aria-hidden="true"></span>
      <h1 class="brand-name">Kind Sparrow<br>Club</h1>
    </div>
    <div class="dot-field" role="img" aria-label="Colourful polka-dot band in pink, orange, teal and purple"></div>
  </section>

</main>
</body>
</html>
```